Brume d'Orvelle Hand Crafted Candles promotional flyer

Hand Crafted Soy Candles - I need a flyer to promote my candles and to give information on care of candles.I want this to use the design and colours I already have for my labels and the photo I have attached.I am aiming at a sophisticated market so would like to reflect this in the design.
Should appeal to sophisticated women who enjoy the pleasure of candles - to enhance their enjoyment of life - gives them the 'brume d'orvelle'.
the candles are hand crafted from all natural ingredients, environmentally friendly and with exquisite fragrances

Target Market(s)

sophisticated females

Industry/Entity Type

Promotional

Font styles to use
Script

Colors
cfeae6
ecdaeb

Requirements
Must have
• something expressing 'brume d'orvelle' - the enjoyment of candles
Should not have
• bright colours

```html
<!DOCTYPE html>
<html lang="en">
<head>
<meta charset="utf-8">
<title>Brume d'Orvelle Hand Crafted Candles</title>
<link href="https://fonts.googleapis.com/css2?family=Berkshire+Swash&display=swap" rel="stylesheet">
<style>
  :root {
    --lilac: #ead9ea;
    --mint: #70c497;
    --salmon: #f2a68e;
    --ink: #1f1a1c;
    --star: #7b2e6c;
    --pale-blue: #d4ecea;
    --photo-dark: #4a4d52;
    --photo-light: #d9d6cf;
    --icon: #2f4a8a;
    --white: #ffffff;
  }
  * { margin: 0; padding: 0; box-sizing: border-box; }
  html, body { width: 1200px; height: 842px; overflow: hidden; background: var(--lilac); }
  body { font-family: 'Berkshire Swash', cursive; color: var(--ink); }
  .flyer { position: relative; width: 1200px; height: 842px; overflow: hidden; background: var(--lilac); }
  .backdrop { position: absolute; inset: 0; }

  .label-box {
    position: absolute;
    background: var(--mint);
    border: 4px solid var(--white);
    border-radius: 14px;
    text-align: center;
    color: var(--ink);
  }
  .title-box { left: 94px; top: 43px; width: 400px; height: 95px; padding-top: 8px; }
  .title-box h1 { font-weight: 400; font-size: 44px; line-height: 1; }
  .title-box p { font-size: 19px; line-height: 1.1; margin-top: 2px; }
  .soy-heading { left: 400px; top: 324px; width: 308px; height: 48px; font-size: 30px; line-height: 40px; }
  .refill-heading { left: 687px; top: 523px; width: 305px; height: 38px; font-size: 23px; line-height: 30px; }

  .star-list { list-style: none; position: absolute; }
  .star-list li { position: relative; padding-left: 32px; }
  .star-list li::before {
    content: "\2605";
    position: absolute; left: 0; top: 0;
    color: var(--star);
    font-family: sans-serif;
    font-size: 0.95em;
  }
  .features { left: 78px; top: 151px; width: 600px; font-size: 16.5px; line-height: 27.5px; }

  .soy-panel {
    position: absolute; left: 240px; top: 381px; width: 680px; height: 134px;
    background: var(--salmon);
  }
  .soy-points { left: 10px; top: 5px; width: 660px; font-size: 15.5px; line-height: 24px; }
  .soy-points li { padding-left: 28px; }

  .refill-points { left: 530px; top: 568px; width: 640px; font-size: 15.5px; line-height: 23.5px; }
  .refill-points li { padding-left: 30px; }

  .contact { position: absolute; left: 815px; top: 710px; list-style: none; font-size: 25px; line-height: 38px; }
  .contact li { display: flex; align-items: center; gap: 14px; }
  .contact svg { width: 18px; height: 18px; flex: none; }

  .brand-seal {
    position: absolute; left: 883px; top: 187px; width: 180px; height: 180px;
    border-radius: 50%;
    background: var(--pale-blue);
    border: 3px solid var(--white);
    display: flex; align-items: center; justify-content: center;
    font-size: 22px; color: var(--ink); text-align: center;
  }
</style>
</head>
<body>
<main class="flyer">
  <svg class="backdrop" width="1200" height="842" viewBox="0 0 1200 842" aria-hidden="true">
    <defs>
      <linearGradient id="topPhotoTone" x1="0" y1="0" x2="1" y2="1">
        <stop offset="0" stop-color="var(--photo-dark)"/>
        <stop offset="0.45" stop-color="var(--photo-light)"/>
        <stop offset="1" stop-color="#8d7c78"/>
      </linearGradient>
      <linearGradient id="bottomPhotoTone" x1="0" y1="0" x2="1" y2="0">
        <stop offset="0" stop-color="#2f3034"/>
        <stop offset="0.5" stop-color="var(--photo-light)"/>
        <stop offset="1" stop-color="#b9b4ad"/>
      </linearGradient>
    </defs>
    <g role="img" aria-label="Photograph of hand-poured soy candles in lidded glass jars on a table">
      <path d="M400,0 H1200 V200 C1100,245 980,262 860,232 C700,190 560,90 400,0 Z" fill="url(#topPhotoTone)"/>
    </g>
    <path d="M430,0 C580,95 720,205 880,240 C990,262 1100,245 1200,205" fill="none" stroke="var(--white)" stroke-width="14"/>
    <g role="img" aria-label="Photograph of a row of soy candles in dark and clear glass jars">
      <path d="M0,690 C80,600 220,560 320,568 C500,585 650,740 800,842 H0 Z" fill="url(#bottomPhotoTone)"/>
    </g>
    <path d="M0,682 C80,592 220,552 320,560 C500,577 650,732 812,842" fill="none" stroke="var(--white)" stroke-width="12"/>
  </svg>

  <header class="label-box title-box">
    <h1>Brume d'Orvelle</h1>
    <p>an exuberant enjoyment of life</p>
  </header>

  <ul class="star-list features">
    <li>These candles will fill you with “Brume d'Orvelle.”</li>
    <li>Candles are lovingly hand-poured and use only the finest of ingredients and fragrances</li>
    <li>Hand crafted soy candle creations</li>
    <li>Completely non-toxic</li>
    <li>Exquisite fragrances</li>
    <li>Clean burning</li>
    <li>Environmentally friendly.</li>
  </ul>

  <div class="brand-seal">Brume d'Orvelle</div>

  <h2 class="label-box soy-heading" style="font-weight:400">Why soy wax?</h2>
  <section class="soy-panel">
    <ul class="star-list soy-points">
      <li>Soft smooth wax that burns clear – no soot or smoke</li>
      <li>Soy wax candles burn up to 50% longer than traditional paraffin candles</li>
      <li>Made from soya beans, a renewable natural resource that supports and sustains agriculture – it is biodegradable and environmentally friendly</li>
      <li>Soy wax burns cooler than paraffin and disperse the fragrance more fully</li>
    </ul>
  </section>

  <h2 class="label-box refill-heading" style="font-weight:400">Containers can be refilled</h2>
  <ul class="star-list refill-points">
    <li>I offer a refill service -if you return you containers to me I can refill with the fragrance of your choice</li>
    <li>Or if you have a special container you would like to use for your candle just contact me for a quote.</li>
    <li>I have a wide range of fragrances - please contact me for details.</li>
  </ul>

  <ul class="contact">
    <li>
      <svg viewBox="0 0 18 18" aria-hidden="true"><circle cx="9" cy="9" r="9" fill="var(--icon)"/><path d="M6,5 L7.5,5 L8.3,7.2 L7.3,8 C7.8,9.2 8.8,10.2 10,10.7 L10.8,9.7 L13,10.5 L13,12 C9,12.5 5.5,9 6,5 Z" fill="var(--white)"/></svg>
      021 555 0148
    </li>
    <li>
      <svg viewBox="0 0 18 18" aria-hidden="true"><circle cx="9" cy="9" r="9" fill="var(--icon)"/><rect x="4.5" y="6" width="9" height="6.5" fill="var(--white)"/><path d="M4.5,6 L9,9.6 L13.5,6" fill="none" stroke="var(--icon)" stroke-width="1"/></svg>
      hello.orvelle@mailbox.co.nz
    </li>
    <li>
      <svg viewBox="0 0 18 18" aria-hidden="true"><circle cx="9" cy="9" r="9" fill="var(--icon)"/><circle cx="9" cy="9" r="4.5" fill="none" stroke="var(--white)" stroke-width="1.2"/><path d="M4.5,9 H13.5 M9,4.5 V13.5" stroke="var(--white)" stroke-width="1"/></svg>
      www.brumedorvelle.co.nz
    </li>
  </ul>
</main>
</body>
</html>
```